Mobile application needs in app icons for a cool new teleportation live broadcast social media app

The app allows you to view a map with your friends on it. Imagine quolby trails but with icons resembling your friends, requests, events that are taking place, and a cluster resembling a lot of activity. The purpose of app is to be able to see on the map what is going on live with your friends all over the world.

We need an avatar for what a person on the map would look like.

We need a request icon that resembles someone requesting an action on that part of the map. Say I want to see a video of the beach and I want to request someone to show me.

We need an icon that resembles an event that is going to take place at that location at a particular time.

We need a cluster icon showing that a lot of activity is taking place in a particular area.

These icons need to stand out and pop out at someone looking at the map and make them interested to want to tap or click on them to see what they are.

```html
<!DOCTYPE html>
<html lang="en">
<head>
<meta charset="utf-8">
<title>Live friend map icons</title>
<link href="https://fonts.googleapis.com/css2?family=Fira+Sans:wght@300;400&display=swap" rel="stylesheet">
<style>
  :root {
    --map-light: #ebe8e1;
    --map-mid: #e2ddd2;
    --map-warm: #ddd6c6;
    --callout-bg: #ffffff;
    --callout-text: #555555;
    --callout-shadow: rgba(0, 0, 0, 0.22);
    --pin-cluster: #d9780f;
    --pin-request: #1a8fe0;
    --pin-avatar: #8fc31f;
    --pin-event: #c3198f;
    --icon-white: #ffffff;
  }
  html, body {
    margin: 0;
    padding: 0;
    overflow: hidden;
    background: var(--map-light);
  }
  .canvas {
    position: relative;
    width: 1200px;
    height: 1200px;
    overflow: hidden;
    font-family: "Fira Sans", sans-serif;
  }
  .map-base {
    position: absolute;
    inset: 0;
    background: linear-gradient(150deg, var(--map-light) 0%, var(--map-mid) 55%, var(--map-warm) 100%);
  }
  .pin {
    position: absolute;
    width: 50px;
    height: 80px;
    filter: drop-shadow(0 2px 2px rgba(0, 0, 0, 0.25));
  }
  .pin--cluster { left: 395px; top: 222px; }
  .pin--request { left: 592px; top: 527px; }
  .pin--avatar  { left: 365px; top: 837px; }
  .pin--event   { left: 464px; top: 897px; }

  .callout {
    position: absolute;
    box-sizing: border-box;
    background: var(--callout-bg);
    border-radius: 8px;
    box-shadow: 0 2px 6px var(--callout-shadow);
    color: var(--callout-text);
    font-weight: 300;
    font-size: 26px;
    line-height: 1.3;
    padding: 12px 22px;
  }
  .callout::before {
    content: "";
    position: absolute;
    left: -14px;
    top: 50%;
    transform: translateY(-50%);
    border-top: 12px solid transparent;
    border-bottom: 12px solid transparent;
    border-right: 14px solid var(--callout-bg);
  }
  .callout--cluster { left: 465px; top: 217px; width: 272px; height: 92px; }
  .callout--request { left: 660px; top: 522px; width: 322px; height: 130px; padding-top: 14px; }
  .callout--avatar  { left: 433px; top: 835px; width: 232px; height: 56px; padding-top: 9px; }
  .callout--event   { left: 524px; top: 893px; width: 276px; height: 92px; }
</style>
</head>
<body>
<div class="canvas">
  <div class="map-base" role="img" aria-label="Street map of a city neighbourhood with roads, a park, schools and freeways"></div>

  <svg class="pin pin--cluster" viewBox="0 0 50 80" aria-hidden="true">
    <path d="M25 78 C20 60 2 48 2 26 A23 23 0 0 1 48 26 C48 48 30 60 25 78 Z" fill="var(--pin-cluster)"/>
    <g fill="var(--icon-white)">
      <circle cx="25" cy="14" r="2.2"/><circle cx="33" cy="17" r="2.2"/>
      <circle cx="36" cy="25" r="2.2"/><circle cx="33" cy="33" r="2.2"/>
      <circle cx="25" cy="36" r="2.2"/><circle cx="17" cy="33" r="2.2"/>
      <circle cx="14" cy="25" r="2.2"/><circle cx="17" cy="17" r="2.2"/>
    </g>
  </svg>
  <div class="callout callout--cluster">Three friends are<br>here.</div>

  <svg class="pin pin--request" viewBox="0 0 50 80" aria-hidden="true">
    <path d="M25 78 C20 60 2 48 2 26 A23 23 0 0 1 48 26 C48 48 30 60 25 78 Z" fill="var(--pin-request)"/>
    <text x="25" y="36" text-anchor="middle" font-family="Fira Sans, sans-serif" font-size="30" font-weight="400" fill="var(--icon-white)">?</text>
  </svg>
  <div class="callout callout--request">Can someone tell me<br>the story behind this<br>park.</div>

  <svg class="pin pin--avatar" viewBox="0 0 50 80" aria-hidden="true">
    <path d="M25 78 C20 60 2 48 2 26 A23 23 0 0 1 48 26 C48 48 30 60 25 78 Z" fill="var(--pin-avatar)"/>
    <circle cx="25" cy="25" r="12" fill="none" stroke="var(--icon-white)" stroke-width="3"/>
  </svg>
  <div class="callout callout--avatar">Studying... :/</div>

  <svg class="pin pin--event" viewBox="0 0 50 80" aria-hidden="true">
    <path d="M25 78 C20 60 2 48 2 26 A23 23 0 0 1 48 26 C48 48 30 60 25 78 Z" fill="var(--pin-event)"/>
    <g fill="none" stroke="var(--icon-white)" stroke-width="2.5">
      <circle cx="19" cy="19" r="5"/>
      <circle cx="31" cy="19" r="5"/>
      <path d="M10 36 C10 28 28 28 28 36 Z"/>
      <path d="M24 30 C28 27 40 28 40 36 L30 36"/>
    </g>
  </svg>
  <div class="callout callout--event">Soccergame at:<br>8 PM, 2013-10-18</div>
</div>
</body>
</html>
```